Silver Creek Plumbing Business card & letter head design

We need a new business card and letter head for our plumbing company called silver creek plumbing. attached is the companys logo. We provide domestic and commercial plumbing services in regional western Australia. We are after Something simple yet nice to look at and something that fits within the trade industry.

Target Market(s)

trade/building industry

Contact Information for Business Card

Darl Hensby
Manager
0461 238 574
enquiries@scplumbwork.net.au
ABN: 47 381 905 462
PCL: 5187

Domestic & Commercial Plumbing
Tip Truck & Excavator hire

Colors

Designer to choose colors to be used in the design.

```html
<!DOCTYPE html>
<html lang="en">
<head>
<meta charset="utf-8">
<title>Silver Creek Plumbing – Business Card</title>
<link rel="stylesheet" href="https://fonts.googleapis.com/css2?family=Arimo:wght@400;700&display=swap">
<style>
  :root {
    --backdrop: #0c2c47;
    --brand-blue: #1d5cc0;
    --brand-blue-dark: #1a4f9e;
    --card-white: #ffffff;
    --band-white: #f3f4f6;
    --ink-grey: #4a4a4c;
    --rule-grey: #9a9a9e;
  }
  * { box-sizing: border-box; margin: 0; padding: 0; }
  html, body {
    width: 1200px; height: 736px; overflow: hidden;
    background: var(--backdrop);
    font-family: "Arimo", Arial, sans-serif;
  }
  .stage { position: relative; width: 1200px; height: 736px; }

  .card {
    position: absolute;
    width: 500px; height: 286px;
    overflow: hidden;
  }

  /* Front */
  .card-front { left: 80px; top: 90px; background: var(--brand-blue); }
  .front-band {
    position: absolute; left: 0; right: 0; top: 78px; height: 130px;
    background: var(--band-white);
  }
  .front-wordmark {
    position: absolute; left: 0; right: 0; top: 128px;
    text-align: center;
    font-weight: 700; font-size: 30px; letter-spacing: 0.5px;
    color: var(--brand-blue-dark);
    text-transform: uppercase;
  }

  /* Back */
  .card-back { left: 620px; top: 360px; background: var(--card-white); }
  .contact-person {
    position: absolute; right: 26px; top: 22px; text-align: right;
  }
  .person-name { font-weight: 700; font-size: 16px; color: var(--brand-blue); }
  .person-role { font-size: 10px; color: var(--ink-grey); margin-top: 1px; }
  .person-phone { font-weight: 700; font-size: 15px; color: var(--ink-grey); margin-top: 2px; }

  .rule { position: absolute; left: 0; right: 0; height: 1.5px; background: var(--rule-grey); }
  .rule-top { top: 108px; }
  .rule-bottom { top: 222px; }

  .edge-tab {
    position: absolute; right: 0; top: 110px; width: 12px; height: 46px;
    background: var(--brand-blue);
  }

  .back-wordmark {
    position: absolute; left: 24px; top: 180px;
    font-weight: 700; font-size: 19px; color: var(--brand-blue-dark);
    text-transform: uppercase;
  }

  .company-details {
    position: absolute; right: 26px; top: 160px; text-align: right;
    font-size: 11.5px; line-height: 1.4; color: var(--ink-grey);
  }

  .services { position: absolute; left: 24px; top: 232px; }
  .service-main { font-weight: 700; font-size: 17px; color: var(--brand-blue); }
  .service-hire { font-weight: 700; font-size: 17px; color: var(--ink-grey); margin-top: 2px; }
</style>
</head>
<body>
<main class="stage">
  <section class="card card-front" aria-label="Business card front">
    <div class="front-band"></div>
    <p class="front-wordmark">Silver Creek Plumbing</p>
  </section>

  <section class="card card-back" aria-label="Business card back">
    <div class="contact-person">
      <p class="person-name">Darl Hensby</p>
      <p class="person-role">Manager</p>
      <p class="person-phone">0461 238 574</p>
    </div>
    <div class="rule rule-top"></div>
    <div class="edge-tab"></div>
    <p class="back-wordmark">Silver Creek Plumbing</p>
    <div class="company-details">
      <p>enquiries@scplumbwork.net.au</p>
      <p>ABN: 47 381 905 462</p>
      <p>PCL: 5187</p>
    </div>
    <div class="rule rule-bottom"></div>
    <div class="services">
      <p class="service-main">Domestic &amp; Commercial Plumbing</p>
      <p class="service-hire">Tip Truck &amp; Excavator hire</p>
    </div>
  </section>
</main>
</body>
</html>
```